Pharmaceutical Manufacturing Services Advertisement

We need a new full page advertisement designed for publication in international magazines. We are a custom pharmaceutical manufacturing company and we help biotechnology companies scale up their drug development for clinical trials. The products we help manufacture are therapeutics for global healthcare problems.

Target Market(s)

Verane Bio is a privately owned contract development manufacturing organisation (CDMO) headquartered in Kellow, QLD, Australia.

Our mission is to is to be a global leader in development and in the provision of contract manufacturing for active pharmaceutical ingredient processes.

Why we do what we Do:

To help advance Biotechnology Companies so that they can deliver innovative therapeutics
~ enabling patients to live longer, healthier and happier lives
~ which solves worldwide health problems

Verane Bio’s role is to develop, implement and scale up the production to deliver biologic medicines for patients in partnership with the biotechnology companies.

Industry/Entity Type

Biotechnology

Font styles to use
Sans Serif

Colors

Designer to choose colors to be used in the design.

Requirements
Must have
• Please see the script on the Word document. There are 4 optional Header Taglines. Additional ideas for multiple designs for the taglines welcomed.
• However preference is for either of the first two:
• 1. Building your vision for better healthcare
• 2. Bridging your vision for better healthcare
• File Specs:
• • All artwork should be submitted as high-resolution (300 min. dpi), press-ready PDF files
• • CMYK color only
• • Full page 8.25” x 10.812”; 209.55 x 274.62 mm
• • Live Area for all sizes: 0.25” (6.35 mm) inside the trim
• • Bleed Area for all sizes: Extends 0.125” (3.175 mm) from trim
Nice to have
• Modern Science look to inspire biotechnology companies to work with us.
• Search for images to use by keyword "recombinant dna"

```html
<!DOCTYPE html>
<html lang="en">
<head>
<meta charset="utf-8">
<title>Verane Bio – Early Phase Clinical Biomanufacturing</title>
<link rel="stylesheet" href="https://fonts.googleapis.com/css2?family=Montserrat:wght@300;400;600;700;800;900&family=Roboto+Condensed:wght@400&display=swap">
<style>
  :root {
    --slate-dark: #353d47;
    --slate-mid: #7c8895;
    --mist: #dfe5ea;
    --paper: #ffffff;
    --lime: #b3c423;
    --lime-bar: #a9bd32;
    --navy: #123f5f;
    --navy-bar: #0d5884;
    --ink: #5a5f66;
    --ink-strong: #4a4f56;
    --helix-red: #d4283d;
    --helix-blue: #3b6fcf;
  }
  * { margin: 0; padding: 0; box-sizing: border-box; }
  html, body { width: 916px; height: 1200px; overflow: hidden; background: var(--paper); }
  .page {
    position: relative;
    width: 916px;
    height: 1200px;
    overflow: hidden;
    background: var(--paper);
    font-family: "Montserrat", Arial, sans-serif;
    color: var(--ink);
  }

  /* Hero */
  .hero-backdrop {
    position: absolute; left: 0; top: 0; width: 916px; height: 690px;
    background: linear-gradient(180deg, var(--slate-dark) 0%, #5d6875 18%, var(--slate-mid) 30%, #c9d1d8 48%, var(--mist) 62%, #f3f5f7 86%, var(--paper) 100%);
  }
  .hero-image {
    position: absolute; left: 0; top: 270px; width: 916px; height: 400px;
    background:
      radial-gradient(ellipse 46% 30% at 48% 28%, rgba(212,40,61,0.85), rgba(212,40,61,0) 70%),
      radial-gradient(ellipse 30% 40% at 46% 55%, rgba(59,111,207,0.75), rgba(59,111,207,0) 70%),
      radial-gradient(ellipse 35% 45% at 8% 55%, rgba(212,40,61,0.75), rgba(59,111,207,0.3) 55%, rgba(59,111,207,0) 75%),
      radial-gradient(ellipse 35% 40% at 88% 62%, rgba(212,40,61,0.75), rgba(59,111,207,0.3) 55%, rgba(59,111,207,0) 75%),
      radial-gradient(ellipse 28% 26% at 42% 80%, rgba(212,40,61,0.7), rgba(212,40,61,0) 70%),
      radial-gradient(ellipse 14% 22% at 92% 8%, rgba(222,196,168,0.9), rgba(222,196,168,0) 70%);
  }
  .headline {
    position: absolute; left: 0; top: 68px; width: 916px;
    text-align: center; text-transform: uppercase;
  }
  .headline-lead {
    display: block; color: var(--paper);
    font-weight: 300; font-size: 45px; letter-spacing: 1.5px; line-height: 52px;
  }
  .headline-accent {
    display: block; color: var(--lime);
    font-weight: 900; font-size: 47px; letter-spacing: 0.5px; line-height: 46px;
  }
  .subheadline {
    position: absolute; left: 0; top: 175px; width: 916px;
    text-align: center; color: var(--paper);
    font-weight: 800; font-size: 19px; letter-spacing: 0.2px;
  }

  /* Body copy */
  .intro {
    position: absolute; left: 76px; top: 692px; width: 770px;
    font-size: 13.4px; line-height: 20px; font-weight: 400; color: var(--ink);
  }
  .intro p + p { margin-top: 20px; }

  /* Lists */
  .offer { position: absolute; left: 78px; width: 380px; }
  .offer-products { top: 870px; }
  .offer-services { top: 999px; }
  .offer-label {
    display: inline-block; height: 21px; padding: 0 12px 0 9px;
    background: var(--lime); color: var(--paper);
    font-weight: 800; font-size: 14.5px; line-height: 22px;
    border-radius: 0 11px 11px 0;
  }
  .offer-list { list-style: none; margin-top: 6px; }
  .offer-services .offer-list { margin-top: 10px; }
  .offer-list li {
    position: relative; padding-left: 17px;
    font-size: 13.6px; line-height: 20px; font-weight: 400; color: var(--ink);
  }
  .offer-list li::before {
    content: ""; position: absolute; left: 2px; top: 7px;
    width: 5px; height: 5px; background: var(--lime);
  }

  /* Brand and contact */
  .brand { position: absolute; left: 526px; top: 930px; width: 300px; }
  .brand-name {
    display: flex; align-items: center; gap: 10px;
    color: var(--navy); font-weight: 700; font-size: 39px; line-height: 46px; letter-spacing: 0.5px;
  }
  .brand-dot { width: 14px; height: 14px; border-radius: 50%; background: var(--navy); }
  .brand-descriptor {
    margin-top: 12px;
    font-family: "Roboto Condensed", "Arial Narrow", sans-serif;
    font-size: 17px; line-height: 20px; color: #2e3d4c; letter-spacing: -0.1px;
  }
  .brand-rule {
    position: absolute; left: 526px; top: 1020px; width: 290px; height: 1px; background: #c3c7cb;
  }
  .contact { position: absolute; left: 526px; top: 1034px; width: 340px; }
  .contact-heading {
    color: var(--lime); font-weight: 800; font-size: 15px; line-height: 20px; letter-spacing: 0.2px;
  }
  .contact-list { list-style: none; margin-top: 5px; }
  .contact-list li {
    display: flex; align-items: center; gap: 8px;
    font-size: 18px; line-height: 26px; color: var(--ink-strong); font-weight: 700;
  }
  .contact-list li.contact-email { font-weight: 400; }
  .contact-icon { width: 16px; height: 16px; flex: none; }

  /* Footer band */
  .footer-band { position: absolute; left: 0; top: 1172px; width: 916px; height: 28px; display: flex; }
  .footer-band-navy { width: 480px; background: var(--navy-bar); }
  .footer-band-lime { flex: 1; background: var(--lime-bar); }
</style>
</head>
<body>
<div class="page">

  <div class="hero-backdrop"></div>
  <div class="hero-image" role="img" aria-label="Photograph of a red and blue DNA double helix with a gloved hand lifting a section away using tweezers"></div>

  <h1 class="headline">
    <span class="headline-lead">Bridging your vision for</span>
    <span class="headline-accent">Better healthcare</span>
  </h1>
  <p class="subheadline">Your Partner in Early Phase Clinical Biomanufacturing</p>

  <div class="intro">
    <p>We have been serving the pharmaceutical, biotechnology and veterinary industry for over 20 years so you can create innovative medicines for worldwide health problems.</p>
    <p>Get your therapeutics to the patient faster with cost-effective manufacturing for your GMP clinical trial material. We offer rapid technology transfer, scale-up development and manufacturing of microbial cell-derived proteins at up to 500L scale. We prepare your active pharmaceutical ingredient (API) products to a world class standard ready for clinical development.</p>
  </div>

  <section class="offer offer-products">
    <h2 class="offer-label">PRODUCTS</h2>
    <ul class="offer-list">
      <li>Recombinant proteins</li>
      <li>Live Biotherapeutics</li>
      <li>Bacterial vaccines</li>
      <li>Plasmid DNA</li>
    </ul>
  </section>

  <section class="offer offer-services">
    <h2 class="offer-label">SERVICES</h2>
    <ul class="offer-list">
      <li>Bacterial / Yeast Fermentation</li>
      <li>Cell Banking</li>
      <li>Process Development/Scale-up</li>
      <li>cGMP Manufacture of biopharmaceutical APIs</li>
      <li>Stability Testing</li>
    </ul>
  </section>

  <div class="brand">
    <div class="brand-name"><span>VERANE BIO</span><span class="brand-dot"></span></div>
    <div class="brand-descriptor">BIOPHARMACEUTICAL MANUFACTURING</div>
  </div>
  <div class="brand-rule"></div>

  <div class="contact">
    <div class="contact-heading">FOR MORE DETAILS PLEASE VISIT</div>
    <ul class="contact-list">
      <li>
        <svg class="contact-icon" viewBox="0 0 16 16" aria-hidden="true">
          <circle cx="8" cy="8" r="6.5" fill="none" stroke="#b3c423" stroke-width="1.6"/>
          <ellipse cx="8" cy="8" rx="2.8" ry="6.5" fill="none" stroke="#b3c423" stroke-width="1.3"/>
          <line x1="1.5" y1="8" x2="14.5" y2="8" stroke="#b3c423" stroke-width="1.3"/>
        </svg>
        veranebio.com.au
      </li>
      <li>
        <svg class="contact-icon" viewBox="0 0 16 16" aria-hidden="true">
          <rect x="0.5" y="0.5" width="15" height="15" rx="3" fill="#b3c423"/>
          <path d="M5 3.5l2 2-1 1.3c.6 1.3 1.7 2.4 3 3l1.3-1 2 2-1.2 1.7C7.6 12.3 3.7 8.4 3.5 4.7z" fill="#fff"/>
        </svg>
        Australia +61(7)35550148
      </li>
      <li class="contact-email">
        <svg class="contact-icon" viewBox="0 0 16 16" aria-hidden="true">
          <rect x="1" y="4" width="14" height="10" fill="#b3c423"/>
          <path d="M1 4l7 5 7-5" fill="none" stroke="#fff" stroke-width="1.3"/>
        </svg>
        enquiries@veranebio.com.au
      </li>
    </ul>
  </div>

  <div class="footer-band">
    <div class="footer-band-navy"></div>
    <div class="footer-band-lime"></div>
  </div>

</div>
</body>
</html>
```